Hunting business need a new wild boar hunting flyer

We need a flyer design for a company based in Saint-Hénédine, Québec. We are a hunting preserve and this flyer must be made for the Boar hunting market. we don’t have any particular restriction for the format but would prefer a tri-fold. The flyer is intended to be given to customer during trade show. You don’t need to put all the information on the flyer I know I have put a lot of info.

85% of our customer are Male with high school or college scholarship.

I may be wrong, but I would like the flyer to have lot’s of black and with a tough style almost like a biker style. Something not clean and hard but with a professional design.

We don’t do standard, don’t be affraid to submit something special even if it required manual assembling. We need something that will mark the customer in the trade show. Note that the custommer receive at least 30 flyers from competitors as well.

Logo of the company in the files.
See files for photo of wild boar.
Would be nice to add wild boar, wild boar skull are pretty impressive (it’s sanglier in french)

Sample text :

Montrez votre côté rebelle!

Offrez-vous LE trip de chasse entre amis !

Chassez en tout temps et sans permis sur deux magnifiques territoires forestiers de la taille de 30 terrains de football chacun. Les enclos sont situés en Beauce, à 30 minutes de Québec. Le taux de succès est de 100 %. Nous pouvons aussi fournir l'hébergement sur demande. La ferme est ouverte depuis 1982 et a toujours été gérée par des passionnés de la chasse, de la nature et de la bonne venaison.

C’est presque « hors-la-loi »!
• Aucun permis requis
• Succès garanti
• Chasse pendant toute l’année
• Guide sur place et territoire exclusif
• À proximité de Québec

Intense et renversant!

Que vous soyez un chasseur débutant ou vétéran, la chasse au sanglier sera pour vous une expérience extraordinaire. Ce gibier, qui ne vit pas à l’état sauvage au Québec, est un adversaire de taille. Ne vous fiez pas à son allure tranquille. S’il se sent en danger, il n’hésite pas à se sauver à toute vitesse et il n’arrête pas, même si vous vous trouvez sur son chemin. Ce gibier est suffisamment gros pour être chassé avec la plupart des carabines. Il se prête aussi très bien à la chasse au fusil, à l’arc ou à l’arbalète.

C’est bien beau, mais ça goûte quoi?

La chair du sanglier est rouge et elle est plus maigre que celle du porc. Elle est très tendre et succulente. Le sanglier offre les mêmes possibilités de coupe que le porc. Vous pouvez aussi l’essayer en méchoui à l’occasion d’une rencontre de groupe. Vos convives et vous dégusterez alors une venaison exceptionnelle.

Quelques commentaires de nos chasseurs :

« J’ai été surpris de voir à quel point ces animaux peuvent se cacher et se déplacer rapidement. C’est beaucoup plus difficile que je croyais. »
Mathieu, Québec, 2015

« La viande était succulente et tendre. J’ai hâte de revenir récolter un autre sanglier à la ferme. »
Josée, Québec, 2015

Réservez pendant le salon et obtenez le crâne blanchi de votre sanglier gratuitement.

Venez récolter les espèces exotiques suivantes :
Cerf de Virginie (500 $*)
Cerf élaphe (850 $*)
Sika (600 $*)
Daim (500 $*)
Dindon sauvage (85 $*)
Faisan (200 $ pour 10)
Sanglier (350 $*)

*Prix de départ, sujet à changement sans préavis.

Le Domaine des Trois Ruisseaux
148, rang Saint-Ovide
Sainte-Alvine (Québec) G0R 4K7

Tél. : 418 237-1046
Courriel : info@boisdorval.ranch
Site Web : www.boisdorval.ranch

Target Market(s)

See description

Industry/Entity Type

Hunting

Requirements
Must have
• Hard, rebel or dirty look.

```html
<!DOCTYPE html>
<html lang="fr">
<head>
<meta charset="utf-8">
<title>Le Domaine des Trois Ruisseaux – dépliant sanglier</title>
<link href="https://fonts.googleapis.com/css2?family=Jost:ital,wght@0,400;0,500;0,600;0,700;1,500&display=swap" rel="stylesheet">
<style>
:root{
  --maroon:#9b2f45;
  --maroon-dark:#7d2236;
  --orange:#e8731f;
  --orange-light:#f39a2c;
  --charcoal:#2b2624;
  --cream:#fbf4c8;
  --cream-deep:#f4e48f;
  --ink:#231f1d;
  --paper:#ffffff;
  --stage:#e4e4e4;
}
*{box-sizing:border-box;margin:0;padding:0}
html,body{width:960px;height:1200px;overflow:hidden;background:var(--stage)}
body{font-family:"Jost",sans-serif;color:var(--ink)}
.spread{position:absolute;left:30px;width:900px;height:560px;display:flex;box-shadow:0 4px 14px rgba(0,0,0,.18)}
.spread--outside{top:30px}
.spread--inside{top:610px}
.panel{position:relative;width:300px;height:560px;overflow:hidden;background:var(--paper)}
.panel + .panel{border-left:1px solid rgba(0,0,0,.08)}
.panel--cream{background:linear-gradient(180deg,var(--cream),var(--cream-deep))}
.photo{position:absolute;left:0;width:300px}
.shapes{position:absolute;inset:0;width:300px;height:560px}
.copy{position:absolute;left:26px;right:26px}
.tick{flex:0 0 11px}

/* outside */
.species__title{top:40px;color:var(--maroon);font-size:18px;font-weight:500;line-height:1.25}
.species__list{top:98px;list-style:none;font-size:17px;line-height:1.4}
.species__note{top:282px;right:70px;color:var(--maroon);font-size:15px;font-weight:600;line-height:1.3}
.offer{top:92px;color:#fff;font-size:17px;font-weight:500;text-align:center;line-height:1.3}
.contact{top:290px;left:40px;color:#fff;font-size:13.5px;line-height:1.45;list-style:none}
.contact li{display:flex;align-items:flex-start;gap:8px}
.contact .icon{flex:0 0 12px;margin-top:4px}
.contact__name{font-weight:500;font-size:14px;padding-left:20px}
.brand{top:40px;text-align:center}
.brand__name{color:var(--maroon);font-weight:600;font-size:21px;line-height:1.15;display:flex;align-items:center;justify-content:center;gap:8px}
.brand__dot{width:10px;height:10px;border-radius:50%;background:var(--maroon);flex:0 0 10px}
.brand__url{margin-top:8px;font-size:12px;color:var(--ink)}
.tagline{top:460px;left:16px;right:16px;text-align:center;color:#fff;line-height:1.25}
.tagline__lead{font-size:18px;font-weight:700;white-space:nowrap}
.tagline__sub{font-size:15px;font-weight:500;margin-top:4px}

/* inside */
.testimonials__title{top:20px;color:#fff;font-size:15px;font-weight:500;line-height:1.25}
.quote{color:#fff;font-size:11px;line-height:1.35;display:flex;gap:6px}
.quote .tick{margin-top:2px}
.quote--first{top:62px}
.quote--second{top:22px;right:60px}
.taste__title{top:200px;color:var(--maroon);font-size:21px;font-weight:600;line-height:1.2}
.body-text{font-size:14px;line-height:1.45;text-align:justify}
.taste__text{top:266px}
.thrill__text{top:140px;font-size:13.5px}
.hunt__text{top:26px;font-size:12.5px;line-height:1.42}
.perks{top:280px}
.perks__title{font-size:13.5px;font-weight:600;color:var(--ink)}
.perks__list{list-style:none;margin-top:4px;color:var(--maroon);font-size:12.5px;line-height:1.45}
.perks__list li{display:flex;align-items:center;gap:6px}
</style>
</head>
<body>

<section class="spread spread--outside">

  <article class="panel panel--species">
    <div class="photo" role="img" aria-label="Photo d'un sanglier debout dans l'herbe sèche" style="top:360px;height:200px;background:linear-gradient(160deg,#8a7a4a,#6b5a36 45%,#4a3b28)"></div>
    <svg class="shapes" viewBox="0 0 300 560" aria-hidden="true">
      <path d="M0 0H300V395Q170 420 0 385Z" fill="var(--paper)"/>
      <path d="M300 318V420H150Z" fill="var(--maroon)"/>
    </svg>
    <h2 class="copy species__title">Venez récolter les espèces exotiques suivantes :</h2>
    <ul class="copy species__list">
      <li>Cerf de Virginie (500 $*)</li>
      <li>Cerf élaphe (850 $*)</li>
      <li>Sika (600 $*)</li>
      <li>Daim (500 $*)</li>
      <li>Dindon sauvage (85 $*)</li>
      <li>Faisan (200 $ pour 10)</li>
      <li>Sanglier (350 $*)</li>
    </ul>
    <p class="copy species__note">*Prix de départ, sujet à changement sans préavis.</p>
  </article>

  <article class="panel panel--contact">
    <div class="photo" role="img" aria-label="Photo d'un sanglier en forêt" style="top:0;height:110px;background:linear-gradient(180deg,#5d5042,#3d332a)"></div>
    <div class="photo" role="img" aria-label="Photo de sous-bois feuillu" style="top:430px;height:130px;background:linear-gradient(170deg,#6b5637,#4a3a28)"></div>
    <svg class="shapes" viewBox="0 0 300 560" aria-hidden="true">
      <path d="M0 40Q150 80 300 60V220Q150 235 0 300Z" fill="var(--maroon)"/>
      <path d="M0 250L100 275L0 305Z" fill="var(--orange)"/>
      <path d="M0 300Q150 235 300 220V430Q150 455 0 505Z" fill="var(--charcoal)"/>
      <path d="M0 505Q150 455 300 430" fill="none" stroke="var(--orange)" stroke-width="7"/>
    </svg>
    <p class="copy offer">Réservez pendant le salon et obtenez le crâne blanchi de votre sanglier gratuitement.</p>
    <ul class="copy contact">
      <li class="contact__name">Le Domaine des Trois Ruisseaux</li>
      <li><svg class="icon" width="12" height="12" viewBox="0 0 12 12"><path d="M6 1a3.5 3.5 0 0 0-3.5 3.5C2.5 7 6 11 6 11s3.5-4 3.5-6.5A3.5 3.5 0 0 0 6 1Z" fill="none" stroke="var(--orange)" stroke-width="1.4"/><circle cx="6" cy="4.5" r="1.2" fill="var(--orange)"/></svg><span>148, rang Saint-Ovide<br>Sainte-Alvine<br>(Québec) G0R 4K7</span></li>
      <li><svg class="icon" width="12" height="12" viewBox="0 0 12 12"><path d="M3 1.5l2 2-1 1.5a6 6 0 0 0 3 3l1.5-1 2 2-1.5 1.5C5 10 2 7 1.5 3Z" fill="var(--orange)"/></svg><span>418 237-1046</span></li>
      <li><svg class="icon" width="12" height="12" viewBox="0 0 12 12"><rect x="1" y="2.5" width="10" height="7" fill="none" stroke="var(--orange)" stroke-width="1.2"/><path d="M1 2.5l5 4 5-4" fill="none" stroke="var(--orange)" stroke-width="1.2"/></svg><span>info@boisdorval.ranch</span></li>
      <li><svg class="icon" width="12" height="12" viewBox="0 0 12 12"><circle cx="6" cy="6" r="4.8" fill="none" stroke="var(--orange)" stroke-width="1.2"/><path d="M1.2 6h9.6M6 1.2c-2.4 3-2.4 6.6 0 9.6M6 1.2c2.4 3 2.4 6.6 0 9.6" fill="none" stroke="var(--orange)" stroke-width="1"/></svg><span>www.boisdorval.ranch</span></li>
    </ul>
  </article>

  <article class="panel panel--cover">
    <div class="photo" role="img" aria-label="Photo d'un chasseur en camouflage tirant à l'arc en forêt" style="top:140px;height:300px;background:linear-gradient(150deg,#7a6a55,#8f8468 40%,#5f6a44 75%,#4d4a36)"></div>
    <svg class="shapes" viewBox="0 0 300 560" aria-hidden="true">
      <path d="M0 0H300V80L230 140Q120 160 0 150Z" fill="#efefef"/>
      <path d="M300 80V150H230Z" fill="var(--maroon)"/>
      <path d="M300 270V405H175Z" fill="var(--maroon)"/>
      <path d="M0 450Q150 420 300 390V560H0Z" fill="var(--charcoal)"/>
      <path d="M0 450Q150 420 300 390" fill="none" stroke="var(--orange)" stroke-width="7"/>
    </svg>
    <header class="copy brand">
      <p class="brand__name"><span class="brand__dot"></span>Le Domaine des<br>Trois Ruisseaux</p>
      <p class="brand__url">www.boisdorval.ranch</p>
    </header>
    <div class="copy tagline">
      <p class="tagline__lead">Montrez votre côté rebelle!</p>
      <p class="tagline__sub">Offrez-vous LE trip de chasse<br>entre amis !</p>
    </div>
  </article>
</section>

<section class="spread spread--inside">

  <article class="panel panel--taste panel--cream">
    <svg class="shapes" viewBox="0 0 300 560" aria-hidden="true">
      <path d="M0 0H300V135Q150 122 0 168Z" fill="var(--maroon)"/>
      <path d="M0 168Q150 122 300 135V155Q150 147 0 195Z" fill="var(--orange)"/>
      <path d="M0 560V520Q150 495 300 470V560Z" fill="var(--orange)"/>
      <path d="M150 560Q230 520 300 505V560Z" fill="var(--maroon)"/>
    </svg>
    <h2 class="copy testimonials__title">Quelques commentaires de nos chasseurs :</h2>
    <p class="copy quote quote--first"><svg class="tick" width="11" height="11" viewBox="0 0 11 11"><circle cx="5.5" cy="5.5" r="4.6" fill="none" stroke="var(--orange)" stroke-width="1.2"/><path d="M3 5.6l1.8 1.8L8 4" fill="none" stroke="var(--orange)" stroke-width="1.3"/></svg><span>« J'ai été surpris de voir à quel point ces animaux peuvent se cacher et se déplacer rapidement. C'est beaucoup plus difficile que je croyais. » Mathieu, Québec, 2015</span></p>
    <h2 class="copy taste__title">C'est bien beau, mais ça goûte quoi?</h2>
    <p class="copy body-text taste__text">La chair du sanglier est rouge et elle est plus maigre que celle du porc. Elle est très tendre et succulente. Le sanglier offre les mêmes possibilités de coupe que le porc. Vous pouvez aussi l'essayer en méchoui à l'occasion d'une rencontre de groupe. Vos convives et vous dégusterez alors une venaison exceptionnelle.</p>
  </article>

  <article class="panel panel--thrill panel--cream">
    <div class="photo" role="img" aria-label="Photo d'un sanglier fouillant le sol" style="top:455px;height:105px;background:linear-gradient(170deg,#7a6850,#54483a)"></div>
    <svg class="shapes" viewBox="0 0 300 560" aria-hidden="true">
      <path d="M0 0H300V50Q150 75 0 115Z" fill="var(--maroon)"/>
      <path d="M0 115Q150 75 300 50V68Q150 95 0 135Z" fill="var(--orange)"/>
      <path d="M0 470Q150 440 300 452V466Q150 456 0 488Z" fill="var(--orange)"/>
    </svg>
    <p class="copy quote quote--second"><svg class="tick" width="11" height="11" viewBox="0 0 11 11"><circle cx="5.5" cy="5.5" r="4.6" fill="none" stroke="var(--orange)" stroke-width="1.2"/><path d="M3 5.6l1.8 1.8L8 4" fill="none" stroke="var(--orange)" stroke-width="1.3"/></svg><span>« La viande était succulente et tendre. J'ai hâte de revenir récolter un autre sanglier à la ferme. » Josée, Québec, 2015</span></p>
    <p class="copy body-text thrill__text">Que vous soyez un chasseur débutant ou vétéran, la chasse au sanglier sera pour vous une expérience extraordinaire. Ce gibier, qui ne vit pas à l'état sauvage au Québec, est un adversaire de taille. Ne vous fiez pas à son allure tranquille. S'il se sent en danger, il n'hésite pas à se sauver à toute vitesse et il n'arrête pas, même si vous vous trouvez sur son chemin. Ce gibier est suffisamment gros pour être chassé avec la plupart des carabines. Il se prête aussi très bien à la chasse au fusil, à l'arc ou à l'arbalète.</p>
  </article>

  <article class="panel panel--hunt panel--cream">
    <div class="photo" role="img" aria-label="Photo d'un sanglier cherchant sa nourriture au sol" style="top:470px;height:90px;background:linear-gradient(160deg,#8a7a68,#6a5c4c 50%,#4c4236)"></div>
    <svg class="shapes" viewBox="0 0 300 560" aria-hidden="true">
      <path d="M0 0H70L0 20Z" fill="var(--maroon)"/>
      <path d="M0 490Q150 450 300 435V470Q150 465 0 505Z" fill="var(--orange)"/>
      <path d="M0 505Q150 465 300 470V478Q150 475 0 513Z" fill="var(--orange-light)"/>
    </svg>
    <p class="copy body-text hunt__text">Chassez en tout temps et sans permis sur deux magnifiques territoires forestiers de la taille de 30 terrains de football chacun. Les enclos sont situés en Beauce, à 30 minutes de Québec. Le taux de succès est de 100 %. Nous pouvons aussi fournir l'hébergement sur demande. La ferme est ouverte depuis 1982 et a toujours été gérée par des passionnés de la chasse, de la nature et de la bonne venaison.</p>
    <div class="copy perks">
      <p class="perks__title">C'est presque « hors-la-loi »!</p>
      <ul class="perks__list">
        <li><svg class="tick" width="10" height="10" viewBox="0 0 11 11"><circle cx="5.5" cy="5.5" r="4.6" fill="none" stroke="var(--orange)" stroke-width="1.2"/><path d="M3 5.6l1.8 1.8L8 4" fill="none" stroke="var(--orange)" stroke-width="1.3"/></svg>Aucun permis requis</li>
        <li><svg class="tick" width="10" height="10" viewBox="0 0 11 11"><circle cx="5.5" cy="5.5" r="4.6" fill="none" stroke="var(--orange)" stroke-width="1.2"/><path d="M3 5.6l1.8 1.8L8 4" fill="none" stroke="var(--orange)" stroke-width="1.3"/></svg>Succès garanti</li>
        <li><svg class="tick" width="10" height="10" viewBox="0 0 11 11"><circle cx="5.5" cy="5.5" r="4.6" fill="none" stroke="var(--orange)" stroke-width="1.2"/><path d="M3 5.6l1.8 1.8L8 4" fill="none" stroke="var(--orange)" stroke-width="1.3"/></svg>Chasse pendant toute l'année</li>
        <li><svg class="tick" width="10" height="10" viewBox="0 0 11 11"><circle cx="5.5" cy="5.5" r="4.6" fill="none" stroke="var(--orange)" stroke-width="1.2"/><path d="M3 5.6l1.8 1.8L8 4" fill="none" stroke="var(--orange)" stroke-width="1.3"/></svg>Guide sur place et territoire exclusif</li>
        <li><svg class="tick" width="10" height="10" viewBox="0 0 11 11"><circle cx="5.5" cy="5.5" r="4.6" fill="none" stroke="var(--orange)" stroke-width="1.2"/><path d="M3 5.6l1.8 1.8L8 4" fill="none" stroke="var(--orange)" stroke-width="1.3"/></svg>À proximité de Québec</li>
      </ul>
    </div>
  </article>
</section>

</body>
</html>
```